Market place for used airplanes/helicopters/parts

http://www.kvistbladet.se needs a facelift.

# What is it
Classifieds for used airplanes/helicopters/parts/spare parts/aviation literature, for people in Scandinavia. The number of classifieds is ~120-200. They are mainly in Swedish, English, Norwegian.

It's not a glamorous or luxurious business, but more for people with a genuine interest in flying, technical things.

Similar to sites like this, but they have much more classifieds than my site
http://www.trevoxlist.com/list/list.aspx?ETID=1&setype=1&catid=6
http://www.bergholmaircraft.com/planes.asp?meny=1&typ=single
https://www.quillhoppers.com/cat.php?mode=listing&main=

# What I want
Design only - no code. I want a modern, maybe a bit bootstrap like, clean, simple, not flashy, web design. I want the design to be in English.

# Audience of the website
Aviation interested men, 45-65 years old, in the nordic countries (around Sweden).

# Logotype that could be used (but not necessarily)
http://www.kvistbladet.se/flygplan_till_salu_large.jpg
http://www.kvistbladet.se/flygplan_till_salu.eps

Reason: I decided to extend the deadline with 1 day. The reason is that I (unfortunately) managed to put the contest in the wrong category for 1 day + I want to give you all feedback (been too busy the whole day, sorry).

Hi all! 

Thanks everyone for the contributions you made. 

I will setup a poll for the designs that I like most. Will get back when I have more information. 

Thanks and have a nice weekend!
Lev

45-65 old Scandinavian men

Business

• - A list with classifieds on the first page, so the visitor easily can see new classifieds.
- A classifieds should be able to have more than one photo
- A simple navigation for showing classifieds from categories like airplanes, helicopters/gyrocopters, parts, literature, misc (maybe other categories) .... but still, it's just 100-200 ads so it's not needed that much filtration.

- A placeholder/way of showing aviation news/clips. In the old design I had, it was a column to the right. It's enough to show maybe 2-5 placeholders.
- A placeholder for PlinkAds ads somewhere on the site.
• - Carousels
- Too much clutter

```html
<!DOCTYPE html>
<html lang="en">
<head>
<meta charset="utf-8">
<title>Vingtorget – Aircraft for sale</title>
<link href="https://fonts.googleapis.com/css2?family=Montserrat:wght@400;500;600;700&display=swap" rel="stylesheet">
<style>
:root{
  --bg-top:#f1f2f3;
  --bg-bottom:#fafafa;
  --card:#ffffff;
  --brand:#1f4f9c;
  --brand-light:#1a8fd0;
  --text:#4a4a4a;
  --muted:#9a9a9a;
  --rule:#d6d6d6;
  --bar:#3a3d40;
  --bar-edge:#2a2c2e;
  --photo-sky:#b9c0c8;
  --photo-ground:#59605a;
}
*{box-sizing:border-box;margin:0;padding:0}
html,body{width:1200px;height:788px;overflow:hidden}
body{background:linear-gradient(var(--bg-top),var(--bg-bottom));font-family:"Montserrat",sans-serif;color:var(--text);position:relative}
.page{position:absolute;left:264px;top:20px;width:672px;height:726px;background:var(--card);border-radius:3px}
.brand{position:absolute;left:14px;top:36px;font-size:22px;font-weight:700;color:var(--brand);letter-spacing:.5px;line-height:26px}
.brand-dot{display:inline-block;width:10px;height:10px;background:var(--brand-light);margin-right:6px;vertical-align:2px}
.search{position:absolute;left:506px;top:33px;width:152px;height:21px;background:var(--brand-light);border-radius:2px;display:flex;align-items:center;padding:3px}
.search input{width:108px;min-width:0;height:14px;border:0;background:#fff;display:block}
.search button{width:38px;border:0;background:transparent;color:#fff;font:700 7px/14px "Montserrat",sans-serif;text-align:center;padding:0}
.hero{position:absolute;left:13px;top:75px;width:645px;height:124px;background:linear-gradient(180deg,#c7c4d4 0%,#bfc6d4 55%,#7d7e82 80%,#9a979a 100%)}
.nav{position:absolute;left:13px;top:199px;width:645px;height:25px;background:var(--bar);border-bottom:1px solid var(--bar-edge);display:flex;align-items:center;box-shadow:0 4px 4px -2px rgba(0,0,0,.12)}
.nav-item{height:25px;display:flex;align-items:center;padding:0 9px;color:#fff;font-size:7.5px;font-weight:700;border-right:1px solid #2b2d2f;white-space:nowrap}
.check{width:8px;height:8px;background:#fff;margin-right:5px;display:inline-flex;align-items:center;justify-content:center}
.show{margin-left:auto;display:flex;align-items:center;color:#fff;font-size:7.5px;padding-right:8px}
.select{width:89px;height:14px;background:#fff;color:#333;margin-left:5px;font-size:7.5px;padding:2px 5px;position:relative}
.select:after{content:"";position:absolute;right:4px;top:5px;border:3px solid transparent;border-top-color:#777}
.view{margin-left:18px;display:flex;gap:8px;align-items:center}
.view svg{display:block}
.listing-box{position:absolute;left:12px;top:237px;width:646px;height:464px;border:1px solid var(--rule)}
.ad{position:absolute;left:9px;width:627px;height:120px}
.rule{position:absolute;left:9px;width:627px;height:1px;background:var(--rule)}
.photo{position:absolute;background:linear-gradient(180deg,var(--photo-sky) 0%,#8f959b 45%,#e8ecef 55%,var(--photo-ground) 80%,#6d7266 100%)}
.photo.main{left:0;top:0;width:154px;height:116px}
.photo.a{left:160px;top:0;width:73px;height:55px}
.photo.b{left:160px;top:61px;width:73px;height:55px}
.ad-body{position:absolute;left:253px;top:0;width:360px;font-size:8.2px;line-height:10.4px}
.ad-title{font-size:15px;line-height:16px;font-weight:700;color:var(--brand);margin-bottom:10px}
.ad-title small{font-size:7px;font-weight:500;color:#333;margin-left:4px}
.ad-body p+p{margin-top:11px}
.pager{position:absolute;left:0;right:0;top:437px;text-align:center;font-size:7.5px}
.pager .off{color:#bbb}
.pager .cur{color:var(--brand);font-weight:700;margin:0 5px}
.pager a{color:#222;text-decoration:none}
.pager .n{text-decoration:underline;margin-right:5px}
.footer{position:absolute;left:279px;top:761px;font-size:7.5px;color:#444}
</style>
</head>
<body>
<div class="page">
  <div class="brand"><span class="brand-dot"></span>VINGTORGET</div>
  <form class="search"><input type="text" aria-label="Search"><button type="button">SEARCH</button></form>
  <div class="hero" role="img" aria-label="Blue and white light aircraft parked on an airfield apron under an overcast sky"></div>
  <nav class="nav">
    <span class="nav-item"><span class="check"><svg width="7" height="7" viewBox="0 0 7 7"><path d="M1 3.5l1.8 2L6 1" fill="none" stroke="#1f4f9c" stroke-width="1.4"/></svg></span>AIRPLANES</span>
    <span class="nav-item"><span class="check"><svg width="7" height="7" viewBox="0 0 7 7"><path d="M1 3.5l1.8 2L6 1" fill="none" stroke="#1f4f9c" stroke-width="1.4"/></svg></span>HELICOPTERS</span>
    <span class="nav-item"><span class="check"></span>PARTS</span>
    <span class="nav-item"><span class="check"></span>SPARE PARTS</span>
    <span class="nav-item"><span class="check"></span>AVIATION LITERATURE</span>
    <div class="show">Show: <span class="select">20 ads</span>
      <span class="view">
        <svg width="12" height="12" viewBox="0 0 12 12" fill="#9a9da0"><rect width="5" height="5"/><rect x="7" width="5" height="5"/><rect y="7" width="5" height="5"/><rect x="7" y="7" width="5" height="5"/></svg>
        <svg width="16" height="16" viewBox="0 0 16 16"><rect width="16" height="16" fill="#ddd"/><rect x="2" y="3" width="5" height="4" fill="#444"/><rect x="2" y="9" width="5" height="4" fill="#444"/><rect x="8" y="3" width="6" height="1.2" fill="#444"/><rect x="8" y="5.5" width="6" height="1.2" fill="#444"/><rect x="8" y="9" width="6" height="1.2" fill="#444"/><rect x="8" y="11.5" width="6" height="1.2" fill="#444"/></svg>
      </span>
    </div>
  </nav>

  <section class="listing-box">
    <article class="ad" style="top:9px">
      <div class="photo main" role="img" aria-label="Single-engine aircraft parked by a hangar"></div>
      <div class="photo a" role="img" aria-label="Aircraft side view"></div>
      <div class="photo b" role="img" aria-label="Aircraft side view"></div>
      <div class="ad-body">
        <h2 class="ad-title">VEGA6<small>AIRPLANES</small></h2>
        <p>Vi sonderar marknaden för vår UL klassade Vega, bygd 1997. Maskinen är i mycket gott skick. 1120tim totalt, 430tim på motor &amp; prop. Flottörfästen installerade.<br>350.000:-<br>Låter det intressant? skicka ett mail.</p>
        <p>Gunnar<br>Namn: Gunnar Lindqvist, E-posta<br>Telefon: 070-5518342<br>Datum: 2013-09-27 06:55:21</p>
      </div>
    </article>
    <div class="rule" style="top:139px"></div>
    <article class="ad" style="top:153px">
      <div class="photo main" role="img" aria-label="Single-engine aircraft parked by a hangar"></div>
      <div class="photo a" role="img" aria-label="Aircraft side view"></div>
      <div class="photo b" role="img" aria-label="Aircraft side view"></div>
      <div class="ad-body">
        <h2 class="ad-title">VEGA6<small>HELICOPTERS</small></h2>
        <p>Vi sonderar marknaden för vår UL klassade Vega, bygd 1997. Maskinen är i mycket gott skick. 1120tim totalt, 430tim på motor &amp; prop. Flottörfästen installerade.<br>350.000:-<br>Låter det intressant? skicka ett mail.</p>
        <p>Gunnar<br>Namn: Gunnar Lindqvist, E-posta<br>Telefon: 070-5518342<br>Datum: 2013-09-27 06:55:21</p>
      </div>
    </article>
    <div class="rule" style="top:282px"></div>
    <article class="ad" style="top:296px">
      <div class="photo main" role="img" aria-label="Single-engine aircraft parked by a hangar"></div>
      <div class="photo a" role="img" aria-label="Aircraft side view"></div>
      <div class="photo b" role="img" aria-label="Aircraft side view"></div>
      <div class="ad-body">
        <h2 class="ad-title">VEGA6<small>HELICOPTERS</small></h2>
        <p>Vi sonderar marknaden för vår UL klassade Vega, bygd 1997. Maskinen är i mycket gott skick. 1120tim totalt, 430tim på motor &amp; prop. Flottörfästen installerade.<br>350.000:-<br>Låter det intressant? skicka ett mail.</p>
        <p>Gunnar<br>Namn: Gunnar Lindqvist, E-posta<br>Telefon: 070-5518342<br>Datum: 2013-09-27 06:55:21</p>
      </div>
    </article>
    <div class="pager"><span class="off">« Previous</span><span class="cur">1</span><a class="n" href="#">2</a><a href="#">Next »</a></div>
  </section>
</div>
<footer class="footer">© 2013 VINGTORGET</footer>
</body>
</html>
```